Qorvane Advisory Corporate Brochure

Qorvane Advisory is a management consulting firm.

We need a corporate brochure showcasing our methodologies (two process diagrams) and our leadership team.

We would like it to look corporate, professional, clean and contemporary.

Happy to have duo tones using our Qorvane logo colours or mono pics.

Also like texture and 3 dimensional backgrounds and graphics.

We are waiting for head and shoulder photos of a couple of our Associate Directors (can you use placeholders while we obtain these please?)

Our web site is:

www.qorvaneadvisory.com.au

Thanks for your ideas.

Industry/Entity Type

Management Consulting

```html
<!DOCTYPE html>
<html lang="en">
<head>
<meta charset="utf-8">
<title>Qorvane Advisory – Brochure Cover</title>
<link rel="stylesheet" href="https://fonts.googleapis.com/css2?family=Arimo:wght@400&display=swap">
<style>
  :root {
    --page-bg: #000000;
    --brand-grey: #4a4d4c;
    --accent-red: #650000;
    --frame-red: #6e0b0b;
    --text-light: #ffffff;
    --hero-light: #e6ebef;
    --hero-teal: #0f5f66;
    --hero-blue: #135f78;
  }
  html, body {
    margin: 0;
    padding: 0;
    overflow: hidden;
    background: var(--page-bg);
  }
  .cover {
    position: relative;
    width: 927px;
    height: 1200px;
    background: var(--page-bg);
    overflow: hidden;
    font-family: "Arimo", Arial, sans-serif;
  }
  .hero-visual {
    position: absolute;
    left: 165px;
    top: 132px;
    width: 726px;
    height: 675px;
    border: 2px solid var(--frame-red);
    background:
      linear-gradient(135deg, transparent 0 14%, var(--hero-teal) 14% 34%, transparent 34% 100%),
      linear-gradient(160deg, transparent 0 46%, var(--hero-blue) 46% 58%, transparent 58% 100%),
      linear-gradient(120deg, #f4f6f8 0%, var(--hero-light) 55%, #c9d0d6 100%);
  }
  .brand-name {
    position: absolute;
    left: 46px;
    bottom: 36px;
    display: flex;
    align-items: center;
    gap: 12px;
    color: var(--brand-grey);
    font-size: 38px;
    font-weight: 400;
    letter-spacing: 0.5px;
  }
  .brand-mark {
    width: 18px;
    height: 18px;
    background: var(--brand-grey);
  }
  .services-panel {
    position: absolute;
    left: 455px;
    top: 924px;
    width: 472px;
    height: 185px;
    box-sizing: border-box;
    padding: 12px 16px 0 15px;
    background: var(--accent-red);
    color: var(--text-light);
  }
  .services-panel p {
    margin: 0;
    font-size: 21.5px;
    line-height: 29px;
  }
</style>
</head>
<body>
  <main class="cover">
    <div class="hero-visual" role="img" aria-label="Abstract 3D wall of white cubes with teal, blue and grey blocks projecting outward"></div>

    <div class="brand-name">
      <span class="brand-mark"></span>
      <span>Qorvane Advisory</span>
    </div>

    <section class="services-panel">
      <p>Qorvane Advisory offers a suite<br>
      of highly effective and useable<br>
      Business Process Improvement,<br>
      Business Strategy and Project<br>
      Management services.</p>
    </section>
  </main>
</body>
</html>
```